Store Front / Boutique Front window signage

I am looking to have a sign printed to stick on the glass of my new Kitchens Cabinets showroom. I already have a logo that I will include however this is the "Boutique" location so I am looking to have my logo incorporated for brand recognition but I do not want just my logo. I want something classy, minimalist with class. Maybe even old school or vintage in style. I will include my store front window sizes and a picture of the store front.

My thought is to take my logo small to moderate in size. Take away the "Cabinetry and Design" part and place that statement larger like this
"Cabinetry and Design Boutique"
My website is Brambleforthkitchens.com
window panes are as follows
left is 72 3/4" wide
right is 70" wide
height is 97 1/2"

I would like to see something not too large , across the two panes
Updates

I have been with work family , looking to choose the best created design and then modify to my liking

Target Market(s)

People !

Font styles to use
Decorative
Script
Other font styles liked:
• vintage , classic

Requirements
Must have
• Tasteful . Maybe logo and small strip along the bottom with a manufacturers logos.
Should not have
• Should not be too large, the signage is not intended to be seen from driving by , more for foot traffic

```html
<!DOCTYPE html>
<html lang="en">
<head>
<meta charset="utf-8">
<title>Brambleforth Kitchens – Boutique Window Signage</title>
<link rel="stylesheet" href="https://fonts.googleapis.com/css2?family=Oswald:wght@500&family=Marcellus&family=Open+Sans:wght@400&display=swap">
<style>
  :root {
    --gold: #dcc46f;
    --paper: #ffffff;
    --backdrop: #ffffff;
    --partner-grey: #5e5e5e;
    --partner-red: #b8322b;
    --partner-dark: #2b2b2b;
  }
  * { margin: 0; padding: 0; box-sizing: border-box; }
  html, body {
    width: 1200px; height: 900px; overflow: hidden;
    background: var(--backdrop);
  }
  .stage { position: relative; width: 1200px; height: 900px; }

  .window-pane {
    position: absolute; top: 100px;
    width: 526px; height: 704px;
    background: var(--paper);
    box-shadow: 0 0 22px rgba(0,0,0,0.14);
  }
  .window-pane--left { left: 34px; }
  .window-pane--right { left: 629px; }

  .brand {
    position: absolute; left: 0; width: 100%;
    color: var(--gold); text-align: center;
    font-family: "Oswald", "Arial Narrow", sans-serif; font-weight: 500;
  }
  .window-pane--left .brand { top: 96px; }
  .window-pane--right .brand { top: 206px; }

  .brand-name {
    font-size: 46px; line-height: 1; letter-spacing: 1px;
  }
  .brand-tagline {
    font-size: 28px; line-height: 1; letter-spacing: 0.5px;
    margin-top: 22px;
  }

  .partners {
    position: absolute; top: 402px; left: 0; width: 100%;
    display: grid; grid-template-columns: 230px 230px;
    justify-content: center; column-gap: 10px; row-gap: 24px;
    align-items: center; justify-items: center;
  }
  .partner {
    display: flex; align-items: center; gap: 7px;
    font-family: "Oswald", "Arial Narrow", sans-serif; font-weight: 500;
    white-space: nowrap; height: 44px;
  }
  .partner__mark { display: inline-block; width: 12px; height: 12px; }
  .partner--ashgrove { color: var(--partner-grey); font-size: 24px; margin-right: 50px; }
  .partner--ashgrove .partner__mark { border-radius: 50%; background: var(--partner-grey); }
  .partner--kestrel { color: var(--partner-dark); font-size: 19px; letter-spacing: 0.5px; }
  .partner--kestrel .partner__mark { border-radius: 50%; background: var(--partner-dark); }
  .partner--vellora { color: var(--partner-red); font-size: 28px; letter-spacing: 4px; margin-right: 50px; }
  .partner--vellora .partner__mark { background: var(--partner-red); }
  .partner--marlowe { color: var(--partner-grey); font-size: 17px; letter-spacing: 3px; }

  .contact {
    position: absolute; top: 528px; left: 0; width: 100%;
    text-align: center; color: var(--gold);
  }
  .contact__phone {
    font-family: "Marcellus", Georgia, serif; font-size: 54px;
    line-height: 1; letter-spacing: 0.5px;
  }
  .contact__web {
    font-family: "Open Sans", Arial, sans-serif; font-size: 21.5px;
    line-height: 1; margin-top: 8px;
  }

  .social {
    position: absolute; top: 620px; left: 0; width: 100%;
    display: flex; justify-content: center; gap: 16px;
  }
  .social__dot {
    width: 43px; height: 43px; border-radius: 50%;
    border: 2px solid var(--gold); padding: 3px;
  }
  .social__dot span {
    display: block; width: 100%; height: 100%;
    border-radius: 50%; background: var(--gold);
  }
</style>
</head>
<body>
<main class="stage">

  <section class="window-pane window-pane--left" aria-label="Left window pane">
    <div class="brand">
      <p class="brand-name">BRAMBLEFORTH KITCHENS</p>
      <p class="brand-tagline">CABINETRY &amp; DESIGN BOUTIQUE</p>
    </div>
    <div class="partners">
      <div class="partner partner--ashgrove"><span class="partner__mark"></span>ashgrove</div>
      <div class="partner partner--kestrel"><span class="partner__mark"></span>Kestrel Cabinetry</div>
      <div class="partner partner--vellora"><span class="partner__mark"></span>VELLORA</div>
      <div class="partner partner--marlowe">MARLOWE KITCHENS</div>
    </div>
    <div class="contact">
      <p class="contact__phone">845-555-0142</p>
      <p class="contact__web">www.brambleforthkitchens.com</p>
    </div>
    <div class="social" aria-label="Social media">
      <div class="social__dot"><span></span></div>
      <div class="social__dot"><span></span></div>
      <div class="social__dot"><span></span></div>
    </div>
  </section>

  <section class="window-pane window-pane--right" aria-label="Right window pane">
    <div class="brand">
      <p class="brand-name">BRAMBLEFORTH KITCHENS</p>
      <p class="brand-tagline">CABINETRY &amp; DESIGN BOUTIQUE</p>
    </div>
    <div class="partners">
      <div class="partner partner--ashgrove"><span class="partner__mark"></span>ashgrove</div>
      <div class="partner partner--kestrel"><span class="partner__mark"></span>Kestrel Cabinetry</div>
      <div class="partner partner--vellora"><span class="partner__mark"></span>VELLORA</div>
      <div class="partner partner--marlowe">MARLOWE KITCHENS</div>
    </div>
    <div class="contact">
      <p class="contact__phone">845-555-0142</p>
      <p class="contact__web">www.brambleforthkitchens.com</p>
    </div>
    <div class="social" aria-label="Social media">
      <div class="social__dot"><span></span></div>
      <div class="social__dot"><span></span></div>
      <div class="social__dot"><span></span></div>
    </div>
  </section>

</main>
</body>
</html>
```